Emergency and Referral Vet Hospital promotional sticker design

We're looking at getting some stickers designed that we could give to clients to put on their cars for promotion and advertising. If they could also be suitable for a goodie bag for conference too that would be great. I like the look of water-colour backgrounds, we'll need to include our logo and probably our address (Unit 3/217 Marlowe Crescent Fairholt). We also have a hospital motto "... because they're family" if that could somehow be integrated, we only care for small animals (dogs, cats etc) but the design is very open to suggestion. Would love to see what you can create.

Industry/Entity Type

Veterinary

Colors
0054AA
0677BA
7BADD7
CADEEF
E8F1F8
0094D4
00A9DD
6FCCEA
C7EBF8
E9F6FB

Requirements
Nice to have
• Think beach vibes, blues maybe paw print shapes etc

```html
<!DOCTYPE html>
<html lang="en">
<head>
<meta charset="utf-8">
<title>Shorewell Referral and Emergency Vet Hospital Sticker</title>
<link rel="stylesheet" href="https://fonts.googleapis.com/css2?family=Open+Sans:ital,wght@0,700;1,600&family=Quicksand:wght@600&display=swap">
<style>
  :root {
    --backdrop: #cbcbcb;
    --sticker: #ffffff;
    --ink-navy: #134b72;
    --ink-plum: #2c1a2d;
    --sand: #f4e8cc;
    --sea-light: #7fd2ea;
    --sea-mid: #2a8fbd;
    --sea-deep: #0f4a78;
    --sea-dark: #143e66;
  }
  * { margin: 0; padding: 0; box-sizing: border-box; }
  html, body {
    width: 1200px;
    height: 1200px;
    overflow: hidden;
    background: var(--backdrop);
  }
  .canvas {
    position: relative;
    width: 1200px;
    height: 1200px;
  }
  .sticker {
    position: absolute;
    left: 334px;
    top: 335px;
    width: 531px;
    height: 531px;
    background: var(--sticker);
    border-radius: 16px;
    overflow: hidden;
  }
  .sticker-art {
    display: block;
    width: 100%;
    height: 100%;
  }
  .headline {
    font-family: "Open Sans", sans-serif;
    font-weight: 700;
    font-size: 35px;
    fill: var(--ink-navy);
    letter-spacing: 0.5px;
  }
  .brand-name {
    font-family: "Open Sans", sans-serif;
    font-weight: 700;
    font-size: 27px;
    fill: var(--ink-plum);
  }
  .motto {
    font-family: "Open Sans", sans-serif;
    font-style: italic;
    font-weight: 600;
    font-size: 19px;
    fill: var(--ink-plum);
  }
  .address {
    font-family: "Quicksand", sans-serif;
    font-weight: 600;
    font-size: 18px;
    fill: var(--sand);
    letter-spacing: 0.4px;
  }
  .phone {
    font-family: "Open Sans", sans-serif;
    font-weight: 700;
    font-size: 49px;
    fill: var(--ink-navy);
  }
</style>
</head>
<body>
<main class="canvas">
  <section class="sticker">
    <svg class="sticker-art" viewBox="0 0 649 649" xmlns="http://www.w3.org/2000/svg">
      <defs>
        <linearGradient id="sea-wash" x1="60" y1="60" x2="600" y2="580" gradientUnits="userSpaceOnUse">
          <stop offset="0" stop-color="var(--sea-light)"/>
          <stop offset="0.35" stop-color="var(--sea-mid)"/>
          <stop offset="0.7" stop-color="var(--sea-deep)"/>
          <stop offset="1" stop-color="var(--sea-dark)"/>
        </linearGradient>
        <path id="headline-arc" d="M 28 198 A 368 368 0 0 1 636 190"/>
        <path id="address-arc" d="M 162 540 Q 330 575 500 548"/>
      </defs>

      <!-- paw print with watercolour wash -->
      <g class="paw" role="img" aria-label="Paw print filled with a blue and teal watercolour wash">
        <g fill="url(#sea-wash)">
          <ellipse cx="249" cy="196" rx="108" ry="135"/>
          <ellipse cx="398" cy="191" rx="110" ry="138"/>
          <ellipse cx="149" cy="338" rx="100" ry="130"/>
          <ellipse cx="498" cy="333" rx="100" ry="130"/>
          <path d="M 325 255 C 470 255 560 380 545 470 C 535 545 470 585 325 578 C 180 585 115 545 105 470 C 90 380 180 255 325 255 Z"/>
        </g>
        <g fill="var(--sticker)">
          <ellipse cx="249" cy="196" rx="60" ry="80"/>
          <ellipse cx="398" cy="191" rx="62" ry="86"/>
          <ellipse cx="149" cy="337" rx="50" ry="83"/>
          <ellipse cx="498" cy="332" rx="50" ry="83" transform="rotate(6 498 332)"/>
          <path d="M 326 303 C 395 303 440 360 460 410 C 480 455 490 495 470 515 C 445 538 390 530 326 530 C 262 530 205 538 180 515 C 162 495 170 455 190 410 C 212 360 258 303 326 303 Z"/>
        </g>
      </g>

      <text class="headline" text-anchor="middle">
        <textPath href="#headline-arc" startOffset="50%">Referral and Emergency Vet Hospital</textPath>
      </text>

      <text class="brand-name" x="326" y="455" text-anchor="middle">Shorewell</text>
      <text class="motto" x="328" y="494" text-anchor="middle">“… because they’re family”</text>

      <text class="address" text-anchor="middle">
        <textPath href="#address-arc" startOffset="50%">Unit 3/217 Marlowe Crescent Fairholt</textPath>
      </text>

      <text class="phone" x="325" y="631" text-anchor="middle">call: (08) 95550142</text>
    </svg>
  </section>
</main>
</body>
</html>
```